Wordpress design for my private practice website - Psychotherapist

I would like a simple, clean, and elegant design for my private practice website. I work with both adults and children so I'd like it to appeal to both. However, since parents make the choice as to where to send their child for therapy, I want it to appeal to adults more. I would like the pictures on the site to have a calming effect - maybe using sand and water and rocks. I am attaching files with my company logo. I would also like my name incorporated into the header - Colette Brannigan, LCSW, Registered Play Therapist. I've also uploaded a picture of myself for my About Page.

I like the design of these 2 website and want something similar:
www.drlorapenwick.example
www.harwood-tallis.example

I would like a home page that highlights a calming graphic across the entire top of the page as well as my practice logo and my name.

I'd like a link to social media sites on the top of the homepage - facebook, pinterest.

I want a simple bar across the top with the following tabs:
Home
About Me (subtabs Who I Am, Specialties and Approach)
Counseling Services (subtabs Individual Counseling, Play Therapy, Sandplay Therapy,)
Fees
FAQs
Contact Me (would love this to be a fill in the blank contact form that sends info to my email address - should include name, phone number, email and a comment box for more information requested)
Blog (this will link with another wordpress blog)

Target Market(s)

Parents of children under age 12 with behavioral problems or are dealing with the breakup of their family through divorce - looking for someone to work with their young child. I also work with Adults that are overwhelmed and worried - often women that have many life stressors and are feeling burnt out on life and meeting everyone's needs. Families going through some type of trauma, including divorce or grief work. I also work with individuals going through a transition of religious beliefs - often exiting the religion of their youth and undergoing a crisis of faith at midlife.

Industry/Entity Type

Mental Health

Contact Information for Business Card

Colette Brannigan, LCSW
Registered Play Therapist
4917 Wexmoor Lane
Idaho Falls, Idaho 83404
(208)555-0187
www.stillbrookcounseling.example

On the opposite side, I'd like an appointment reminder area - with the following text:

Your next appointment is
_____/______/______ at ______am/pm
Please give 24 hrs notice if you need to cancel your appointment.

Coding

Coded - Design and coding required

Number of Pages Required

5+ page

Font styles to use
Sans Serif

Colors
33a6d7
9bcb3c
0355a3

Requirements
Must have
• I'd like it to be a wordpress site. I'm such a newby at web design - but I need to be able to add content and manage the site myself once it is up and running.
Nice to have
• I like the design of these 2 websites and want something similar:
• www.drlorapenwick.example
• www.harwood-tallis.example
• They are clean, easy to navigate and calming.
Should not have
• Should not look like a childcare website.

```html
<!DOCTYPE html>
<html lang="en">
<head>
<meta charset="utf-8">
<title>Stillbrook Counseling</title>
<link href="https://fonts.googleapis.com/css2?family=PT+Sans:wght@400;700&display=swap" rel="stylesheet">
<style>
:root{
  --sky:#33a6d7;
  --leaf:#9bcb3c;
  --navy:#0355a3;
  --title:#0d5ba8;
  --ink:#555;
  --nav:#333;
  --rule:#1c63ad;
}
*{margin:0;padding:0;box-sizing:border-box}
html,body{width:934px;height:1200px;overflow:hidden;background:#fff}
body{position:relative;font-family:"PT Sans",sans-serif;color:var(--ink)}
.abs{position:absolute}
/* header */
.brand{left:195px;top:14px;display:flex;align-items:center;gap:6px;font-size:13px;color:var(--navy);letter-spacing:1px}
.brand .dot{width:12px;height:12px;border-radius:50%;background:var(--leaf)}
.nav a{position:absolute;top:29px;font-size:10px;color:var(--nav);text-decoration:none;white-space:nowrap}
.nav a.current{color:var(--sky);border-bottom:2px solid var(--sky);padding-bottom:2px}
.dropdown{left:449px;top:54px;width:135px;background:var(--sky);border-bottom:2px solid var(--navy)}
.dropdown div{height:21px;line-height:21px;padding-left:10px;font-size:8px;color:#fff;border-bottom:1px solid rgba(255,255,255,.45)}
.dropdown div:last-child{border:0;color:var(--navy)}
.dropdown:before{content:"";position:absolute;top:-4px;left:40px;border:4px solid transparent;border-top:0;border-bottom-color:var(--sky)}
/* hero */
.hero{left:0;top:58px;width:934px;height:243px;background:radial-gradient(ellipse at 45% 40%,#fbfbfa 0%,#e7e9e4 45%,#c9cfc4 75%,#aab59f 100%)}
.dots{left:455px;top:287px;display:flex;gap:5px}
.dots span{width:5px;height:5px;border-radius:50%;background:var(--sky)}
.dots span.on{background:var(--navy)}
/* section titles */
.title{left:0;width:934px;text-align:center;font-size:14px;color:var(--title)}
.rule{left:306px;width:322px;height:8px}
/* about */
.portrait{left:194px;top:356px;width:107px;height:82px;background:linear-gradient(135deg,#e9d4a2,#c9a46a 55%,#7a6a55)}
.name{left:308px;top:358px;font-size:11px;color:var(--sky)}
.bio{left:308px;top:372px;width:425px;font-size:7px;line-height:9.6px}
.btn{background:var(--leaf);color:#2f3a16;text-align:center;font-size:8px}
/* cards */
.card .img{position:absolute;left:0;top:0;width:62px;height:61px;border:1px solid #9aa}
.card h3{position:absolute;left:68px;top:0;font-size:7px;color:var(--sky);font-weight:700;white-space:nowrap}
.card p{position:absolute;left:68px;top:11px;width:98px;height:29px;overflow:hidden;font-size:5.2px;line-height:7.2px}
.card .btn{position:absolute;left:67px;top:46px;width:92px;height:15px;line-height:15px;font-size:7.5px}
/* fees */
.fees{left:196px;top:718px;width:546px;font-size:8px;line-height:9.8px;color:#666}
.checks{left:220px;top:759px;list-style:none;font-size:7px;color:var(--sky)}
.checks li{height:17.8px;display:flex;gap:6px;align-items:flex-start}
/* blog */
.post-img{left:194px;top:883px;width:206px;height:140px;border:1px solid #9aa;background:linear-gradient(160deg,#eef1f3,#c9d0d6 55%,#7f8790)}
.post-title{left:405px;top:883px;font-size:11px;color:var(--sky)}
.post-text{left:405px;top:907px;width:325px;font-size:7px;line-height:9.6px}
.meta{left:405px;top:951px;font-size:6px;color:var(--navy);display:flex;gap:3px;align-items:center}
.icons{left:405px;top:976px;display:flex;gap:7px}
.arrows{left:712px;top:1010px;display:flex}
.arrows span{width:14px;height:12px;border:1px solid #999;font-size:8px;line-height:10px;text-align:center;color:#333}
/* footer */
.footer{left:0;top:1045px;width:934px;height:155px;background:var(--navy)}
.f-head{font-size:11px;color:#fff}
.f-bar{width:74px;height:3px;background:var(--sky)}
.f-lead{left:194px;top:1092px;width:200px;font-size:8.5px;line-height:11px;color:var(--leaf);font-weight:700}
.f-input{left:194px;top:1128px;width:128px;height:15px;background:#1e6cc0;font-size:5px;color:#7ba8d8;padding:5px 3px}
.f-btn{left:324px;top:1128px;width:53px;height:15px;line-height:15px;font-size:8px;color:var(--navy)}
.f-text{font-size:8px;color:#dfe9f5;line-height:10px}
.f-line{left:0;top:1167px;width:934px;height:1px;background:#2c74bb}
.copy{left:0;top:1179px;width:934px;text-align:center;font-size:5px;color:#b9cde6}
</style>
</head>
<body>

<header>
  <div class="abs brand"><span class="dot"></span>STILLBROOK COUNSELING</div>
  <nav class="nav">
    <a class="current" style="left:337px">Home</a>
    <a style="left:386px">About Me ▾</a>
    <a class="current" style="left:450px">Counseling Services</a>
    <a style="left:557px">Fees</a>
    <a style="left:601px">FAQs</a>
    <a style="left:648px">Contact Me</a>
    <a style="left:718px">Blog</a>
  </nav>
  <div class="abs dropdown">
    <div>subtabs Individual Counseling</div>
    <div>Play Therapy</div>
    <div>Sandplay Therapy</div>
  </div>
</header>

<div class="abs hero" role="img" aria-label="Close-up of white snowdrop flowers"></div>
<div class="abs dots"><span></span><span class="on"></span><span></span></div>

<h2 class="abs title" style="top:314px">About ME</h2>
<svg class="abs rule" style="top:334px" viewBox="0 0 322 8"><path d="M0 4H154l3-3 3 6 3-4 2 1H322" fill="none" stroke="var(--rule)" stroke-width="1"/></svg>
<div class="abs portrait" role="img" aria-label="Portrait photo of the therapist"></div>
<div class="abs name">Dr. Miriam Harwood-Tallis</div>
<p class="abs bio">I am a licensed psychotherapist with a Ph.D in Counseling Psychology from Eastbrook College. I wrote my dissertation on LDS women and sexuality, have taught college-level courses on human sexuality, and currently teach online and community-based relationship and sexuality courses to LDS couples.</p>
<div class="abs btn" style="left:309px;top:418px;width:80px;height:20px;line-height:20px">Read More</div>

<h2 class="abs title" style="top:466px">Specialties &amp; Approach</h2>
<svg class="abs rule" style="top:487px" viewBox="0 0 322 8"><path d="M0 4H154l3-3 3 6 3-4 2 1H322" fill="none" stroke="var(--rule)" stroke-width="1"/></svg>

<div class="abs card" style="left:194px;top:511px">
  <div class="img" role="img" aria-label="Couple sharing a kiss at a café table" style="background:linear-gradient(135deg,#8a6b58,#d8b7a6 60%,#e9c8cf)"></div>
  <h3>RELATIONSHIP COUNSELING</h3>
  <p>Do you long to feel more loved and appreciated by your partner? Are you tired of the unproductive fights? Is the unhappiness causing the two of</p>
  <div class="btn">Read More</div>
</div>
<div class="abs card" style="left:382px;top:511px">
  <div class="img" role="img" aria-label="Couple in dramatic low light" style="background:linear-gradient(135deg,#2a1c16,#7a4a35 55%,#1a1210)"></div>
  <h3>SEXUALITY</h3>
  <p>Almost all couples deal with sexual issues at some point in the course of long-term relationships. Because sexual problems affect how people</p>
  <div class="btn">Read More</div>
</div>
<div class="abs card" style="left:574px;top:511px">
  <div class="img" role="img" aria-label="Person sitting with head resting on knees" style="background:linear-gradient(135deg,#cfd4d8,#6f7780 55%,#2e3640)"></div>
  <h3>DEPRESSION</h3>
  <p>The National Wellness Survey estimates that approximately 17 million American adults suffer from depression each year. Often</p>
  <div class="btn">Read More</div>
</div>
<div class="abs card" style="left:194px;top:591px">
  <div class="img" role="img" aria-label="Women talking over coffee" style="background:linear-gradient(135deg,#c98a55,#e8c7a6 55%,#8a5a3a)"></div>
  <h3>WOMEN'S ISSUES</h3>
  <p>I have a particular passion for helping women. I studied women's studies as an undergraduate and feminist-relational models of therapy in gradu-</p>
  <div class="btn">Read More</div>
</div>
<div class="abs card" style="left:382px;top:591px">
  <div class="img" role="img" aria-label="Silhouette meditating against a purple sky over water" style="background:linear-gradient(180deg,#8d86c4,#c9b0c9 55%,#3a4f7a)"></div>
  <h3>SPIRITUALITY &amp; IDENTITY</h3>
  <p>Spirituality is about finding an inner compass that guides you and gives you strength. Identifying and trusting this source of wisdom is an</p>
  <div class="btn">Read More</div>
</div>
<div class="abs card" style="left:574px;top:591px">
  <div class="img" role="img" aria-label="Mother and young son smiling together" style="background:linear-gradient(135deg,#f2dcc4,#d9a77e 55%,#b8703f)"></div>
  <h3>PARENTING</h3>
  <p>Do you have a difficult teenager or young child? Do you feel unclear about how and where to set limits, or how to respond to disobedience?</p>
  <div class="btn">Read More</div>
</div>

<h2 class="abs title" style="top:679px">Fees</h2>
<svg class="abs rule" style="top:700px" viewBox="0 0 322 8"><path d="M0 4H154l3-3 3 6 3-4 2 1H322" fill="none" stroke="var(--rule)" stroke-width="1"/></svg>
<p class="abs fees">In addition to counseling and consultation with individuals, couples, and families (in person and online), she provides program evaluation and consulting services for fertility clinics, and is also available to lead clinic workshops that are research-proven to boost fertility and help patients cope with the treatment process.</p>
<ul class="abs checks">
  <li><svg width="9" height="8" viewBox="0 0 9 8"><rect x=".5" y="1.5" width="6" height="6" fill="none" stroke="var(--navy)"/><path d="M2 4l2 2 4-5" fill="none" stroke="var(--navy)" stroke-width="1.4"/></svg>Your partner is distant, withdrawn, or unemotional.</li>
  <li><svg width="9" height="8" viewBox="0 0 9 8"><rect x=".5" y="1.5" width="6" height="6" fill="none" stroke="var(--navy)"/><path d="M2 4l2 2 4-5" fill="none" stroke="var(--navy)" stroke-width="1.4"/></svg>You have feelings that you seem unable to communicate to your partner.</li>
  <li><svg width="9" height="8" viewBox="0 0 9 8"><rect x=".5" y="1.5" width="6" height="6" fill="none" stroke="var(--navy)"/><path d="M2 4l2 2 4-5" fill="none" stroke="var(--navy)" stroke-width="1.4"/></svg>Your partner seems chronically dissatisfied with you.</li>
  <li><svg width="9" height="8" viewBox="0 0 9 8"><rect x=".5" y="1.5" width="6" height="6" fill="none" stroke="var(--navy)"/><path d="M2 4l2 2 4-5" fill="none" stroke="var(--navy)" stroke-width="1.4"/></svg>You and your partner have the same fight over and over.</li>
</ul>

<h2 class="abs title" style="top:846px">Latest Blog</h2>
<svg class="abs rule" style="top:867px" viewBox="0 0 322 8"><path d="M0 4H154l3-3 3 6 3-4 2 1H322" fill="none" stroke="var(--rule)" stroke-width="1"/></svg>
<div class="abs post-img" role="img" aria-label="Couple embracing in a snowy park"></div>
<div class="abs post-title">HOLIDAY SALE: 20 % OFF ALL COURSES!</div>
<p class="abs post-text">Four acclaimed online courses are available for a limited time at 20 % OFF! (deeper discounts available when you purchase more than one course). Three courses include outlines, assignments, and video recordings (from live workshops), delivered electronically. The fourth is the newly redesigned learning management system. To learn more,</p>
<div class="abs meta"><svg width="7" height="7" viewBox="0 0 8 8"><circle cx="4" cy="4" r="3.3" fill="none" stroke="var(--navy)"/><path d="M4 2v2h2" fill="none" stroke="var(--navy)"/></svg>23 Feb 2016</div>
<div class="abs icons">
  <svg width="9" height="8" viewBox="0 0 9 8"><ellipse cx="4.5" cy="3.5" rx="3.8" ry="2.8" fill="none" stroke="var(--navy)"/><path d="M2 6l-1 2 3-1.5" fill="var(--navy)"/></svg>
  <svg width="9" height="8" viewBox="0 0 9 8"><path d="M4.5 7.5L1 4a2 2 0 013.5-2.5A2 2 0 018 4z" fill="var(--navy)"/></svg>
  <svg width="8" height="8" viewBox="0 0 8 8"><circle cx="6" cy="1.5" r="1.4" fill="var(--navy)"/><circle cx="6" cy="6.5" r="1.4" fill="var(--navy)"/><circle cx="1.8" cy="4" r="1.4" fill="var(--navy)"/><path d="M6 1.5L2 4l4 2.5" fill="none" stroke="var(--navy)"/></svg>
</div>
<div class="abs btn" style="left:405px;top:1000px;width:135px;height:22px;line-height:22px;font-size:9px">Read More</div>
<div class="abs arrows"><span>‹</span><span>›</span></div>

<footer class="abs footer"></footer>
<div class="abs f-head" style="left:194px;top:1062px">SIGN UP</div>
<div class="abs f-bar" style="left:194px;top:1080px"></div>
<div class="abs f-lead">RECEIVE SPECIAL OFFERS AND UPDATES ON MIRIAM'S WORK. SIGN UP NOW!</div>
<div class="abs f-input">ENTER EMAIL</div>
<div class="abs btn f-btn">SIGN UP</div>

<div class="abs f-head" style="left:443px;top:1061px">ADDRESS</div>
<div class="abs f-bar" style="left:443px;top:1079px"></div>
<div class="abs f-text" style="left:443px;top:1094px;display:flex;gap:4px"><svg width="6" height="9" viewBox="0 0 6 9"><path d="M3 9L.5 4a2.6 2.6 0 115 0z" fill="var(--leaf)"/><circle cx="3" cy="3" r="1" fill="var(--navy)"/></svg><span>1382 Alder Row, Marlow, GA<br>30699, United States</span></div>
<div class="abs f-text" style="left:443px;top:1122px;display:flex;gap:4px"><svg width="8" height="8" viewBox="0 0 8 8"><path d="M1 1l2-.5 1 2-1 1a5 5 0 002 2l1-1 2 1-.5 2C3 8 0 4 1 1z" fill="var(--leaf)"/></svg>847-555-0162</div>
<div class="abs f-text" style="left:443px;top:1138px;display:flex;gap:4px;align-items:center"><svg width="8" height="6" viewBox="0 0 8 6"><rect width="8" height="6" fill="var(--leaf)"/><path d="M0 0l4 3 4-3" fill="none" stroke="var(--navy)" stroke-width=".8"/></svg>miriam@harwood-tallis.example</div>

<div class="abs f-head" style="left:629px;top:1061px">LINK</div>
<div class="abs f-bar" style="left:629px;top:1079px"></div>
<div class="abs f-text" style="left:629px;top:1094px">Subtabs Individual Counseling</div>
<div class="abs f-text" style="left:629px;top:1111px">Play Therapy</div>
<div class="abs f-text" style="left:630px;top:1128px">Sandplay Therapy</div>

<div class="abs f-line"></div>
<div class="abs copy">© 2016 Miriam Harwood-Tallis. All rights reserved.</div>

</body>
</html>
```